I am looking for a design for my business card. I need a logo. The company is called Harborline Capital. We are an investment management and technology consulting company. I am looking for a professional conservative design. I think a lighthouse might be a good simple for us.

For the business card.
company URL www.harborlinecapital.example
my name: Philip R. Kessler
email: pkessler@harborlinecapital.example
my phone # 318-469-5730

Contact Information for Business Card

company URL www.harborlinecapital.example my name: Philip R. Kessler email: pkessler@harborlinecapital.example my phone # 318-469-5730

Colors
0054AA
0677BA
7BADD7
CADEEF
E8F1F8

Requirements
Must have
• area on the back for a QR code

```html
<!DOCTYPE html>
<html lang="en">
<head>
<meta charset="utf-8">
<title>Harborline Capital — Business Card</title>
<link rel="stylesheet" href="https://fonts.googleapis.com/css2?family=Crimson+Text:wght@400;600&display=swap">
<style>
  :root {
    --navy: #1256a8;
    --blue: #0054aa;
    --mid-blue: #0677ba;
    --ink: #3b3b3b;
    --paper: #ffffff;
    --backdrop: #e4e6e8;
  }
  * { margin: 0; padding: 0; box-sizing: border-box; }
  html, body { width: 1080px; height: 1200px; overflow: hidden; }
  body {
    position: relative;
    font-family: "Crimson Text", Georgia, serif;
    background: var(--backdrop);
  }
  .card-stage {
    position: absolute; left: 0; top: 0;
    width: 1080px; height: 807px;
    background: var(--backdrop);
  }
  .card {
    position: absolute; left: 186px; top: 200px;
    width: 708px; height: 406px;
    background: var(--paper);
    box-shadow: 0 10px 24px rgba(0,0,0,0.18);
  }
  .card__band { position: absolute; left: 0; width: 100%; background: var(--navy); }
  .card__band--top { top: 0; height: 28px; }
  .card__band--bottom { bottom: 0; height: 31px; }
  .card__brand {
    position: absolute; left: 330px; top: 62px;
    display: flex; align-items: center; gap: 12px;
  }
  .brand-mark { width: 22px; height: 22px; border-radius: 50%; background: var(--navy); }
  .brand-name {
    font-weight: 600; font-size: 38px; line-height: 1;
    color: var(--navy); white-space: nowrap;
  }
  .card__identity {
    position: absolute; left: 22px; top: 100px;
    text-align: right;
  }
  .identity__name {
    font-weight: 600; font-size: 37px; line-height: 1; color: var(--navy);
  }
  .identity__role {
    font-size: 24px; line-height: 1.1; color: var(--ink); letter-spacing: 0.5px;
  }
  .contact-list { position: absolute; left: 24px; top: 215px; list-style: none; }
  .contact-item {
    display: flex; align-items: center; gap: 17px;
    height: 28px; margin-bottom: 27px;
    font-size: 23px; color: var(--ink);
  }
  .contact-item svg { width: 28px; height: 28px; flex: none; }
  .qr-area {
    position: absolute; left: 461px; top: 187px;
    width: 169px; height: 168px;
    border: 3px solid var(--navy); border-radius: 14px;
  }
  .logo-panel {
    position: absolute; top: 807px; height: 393px;
    display: flex; align-items: center; justify-content: center; gap: 16px;
  }
  .logo-panel--light { left: 0; width: 541px; background: var(--paper); }
  .logo-panel--dark { left: 541px; width: 539px; background: var(--navy); }
  .logo-panel .brand-name { font-size: 52px; }
  .logo-panel .brand-mark { width: 30px; height: 30px; }
  .logo-panel--dark .brand-name { color: var(--paper); }
  .logo-panel--dark .brand-mark { background: var(--paper); }
</style>
</head>
<body>
  <section class="card-stage">
    <article class="card">
      <div class="card__band card__band--top"></div>

      <div class="card__brand">
        <span class="brand-mark"></span>
        <span class="brand-name">Harborline Capital</span>
      </div>

      <div class="card__identity">
        <div class="identity__name">Philip R. Kessler</div>
        <div class="identity__role">DESIGNATION</div>
      </div>

      <ul class="contact-list">
        <li class="contact-item">
          <svg viewBox="0 0 28 28" aria-hidden="true">
            <circle cx="14" cy="14" r="14" fill="var(--navy)"/>
            <path d="M9.5 7.5l3 3-1.6 1.8c.9 2 2.3 3.4 4.3 4.3l1.8-1.6 3 3-2 2c-5 0-10.5-5.5-10.5-10.5z" fill="#fff"/>
          </svg>
          <span>318-469-5730</span>
        </li>
        <li class="contact-item">
          <svg viewBox="0 0 28 28" aria-hidden="true">
            <circle cx="14" cy="14" r="14" fill="var(--navy)"/>
            <rect x="7.5" y="9.5" width="13" height="9" fill="#fff"/>
            <path d="M7.5 9.5l6.5 5 6.5-5M7.5 18.5l4.8-4.2M20.5 18.5l-4.8-4.2" fill="none" stroke="var(--navy)" stroke-width="1"/>
          </svg>
          <span>pkessler@harborlinecapital.example</span>
        </li>
        <li class="contact-item">
          <svg viewBox="0 0 28 28" aria-hidden="true">
            <circle cx="14" cy="14" r="14" fill="var(--navy)"/>
            <g fill="none" stroke="#fff" stroke-width="1.2">
              <circle cx="14" cy="14" r="7.5"/>
              <ellipse cx="14" cy="14" rx="3.2" ry="7.5"/>
              <path d="M6.5 14h15M8 10h12M8 18h12"/>
            </g>
          </svg>
          <span>www.harborlinecapital.example</span>
        </li>
      </ul>

      <div class="qr-area" aria-label="Space for QR code"></div>

      <div class="card__band card__band--bottom"></div>
    </article>
  </section>

  <section class="logo-panel logo-panel--light">
    <span class="brand-mark"></span>
    <span class="brand-name">Harborline Capital</span>
  </section>
  <section class="logo-panel logo-panel--dark">
    <span class="brand-mark"></span>
    <span class="brand-name">Harborline Capital</span>
  </section>
</body>
</html>
```